Quill Athletics Flyer

Need a flyer to showcase my fitness facility with a focus on "PERSONAL TRAINING". To be used in paper advertisements.

I've added some photos below. Please make sure to use our logo as well as the pictures below (use as many as you like).

Also please make sure to add our contact info:

4-18 263rd st.
Whitestone NY, 11357

718-403-5816

contact@quillathletic.com

Lastly please make sure to add a "Contact us for a free trial!" stamp somewhere on the page.

```html
<!DOCTYPE html>
<html lang="en">
<head>
<meta charset="utf-8">
<title>Quill Athletics Flyer</title>
<link rel="stylesheet" href="https://fonts.googleapis.com/css2?family=Archivo+Black&family=Open+Sans:wght@300;400;800&display=swap">
<style>
  :root {
    --lime: #a9c23c;
    --lime-deep: #84a52a;
    --white: #ffffff;
    --ink: #2a2a2a;
    --frame: #ebe7f0;
    --shadow: rgba(40, 60, 10, 0.35);
  }
  * { margin: 0; padding: 0; box-sizing: border-box; }
  html, body { width: 970px; height: 1200px; overflow: hidden; background: var(--white); }
  .flyer {
    position: relative;
    width: 970px;
    height: 1200px;
    background: var(--lime);
    overflow: hidden;
    font-family: "Open Sans", sans-serif;
  }
  .headline-word {
    position: absolute;
    left: 0;
    font-family: "Archivo Black", sans-serif;
    color: var(--lime-deep);
    line-height: 1;
    white-space: nowrap;
    letter-spacing: -2px;
  }
  .headline-top { top: -20px; left: 50px; font-size: 205px; }
  .headline-bottom { top: 752px; left: 60px; font-size: 318px; letter-spacing: -4px; }
  .callout {
    position: absolute;
    left: 0;
    width: 100%;
    text-align: center;
    color: var(--white);
    font-weight: 800;
    font-size: 36px;
    letter-spacing: 0.2px;
  }
  .callout-trial { top: 195px; }
  .callout-phone { top: 720px; }
  .snapshot {
    position: absolute;
    background: var(--frame);
    box-shadow: 4px 6px 10px var(--shadow);
    padding: 18px 18px 80px;
  }
  .snapshot .photo { width: 100%; height: 100%; }
  .snapshot-left { left: -20px; top: 296px; width: 334px; height: 394px; transform: rotate(-2deg); }
  .snapshot-center { left: 308px; top: 282px; width: 352px; height: 404px; transform: rotate(1.5deg); }
  .snapshot-right { left: 668px; top: 290px; width: 330px; height: 386px; transform: rotate(-3deg); }
  .photo-ropes { background: linear-gradient(135deg, #6fa7d6 0%, #c9d6d2 40%, #3a5fb0 75%, #2b3a6a 100%); }
  .photo-straps { background: linear-gradient(135deg, #7a5a45 0%, #c79a80 40%, #8d6fa0 70%, #3f3640 100%); }
  .photo-sled { background: linear-gradient(160deg, #e6e2dc 0%, #b9a8a8 45%, #8a6f86 80%, #4c3a4a 100%); }
  .info-band {
    position: absolute;
    left: 0;
    top: 1018px;
    width: 100%;
    height: 182px;
    background: var(--white);
  }
  .contact-list { position: absolute; left: 70px; top: 22px; list-style: none; }
  .contact-item {
    position: relative;
    padding-left: 44px;
    font-weight: 300;
    font-size: 20px;
    line-height: 25px;
    color: var(--ink);
    text-transform: uppercase;
    margin-bottom: 14px;
  }
  .contact-icon { position: absolute; left: 0; top: 0; width: 30px; height: 30px; }
  .brand { position: absolute; left: 578px; top: 40px; width: 330px; text-align: center; }
  .brand-name {
    display: flex;
    align-items: center;
    justify-content: center;
    gap: 12px;
    font-family: "Archivo Black", sans-serif;
    font-size: 34px;
    color: var(--ink);
    letter-spacing: 1px;
    text-transform: uppercase;
  }
  .brand-dot { width: 30px; height: 30px; border-radius: 50%; background: var(--lime); flex: none; }
  .brand-tagline {
    margin-top: 12px;
    font-size: 17px;
    letter-spacing: 3px;
    color: var(--ink);
    text-transform: uppercase;
  }
</style>
</head>
<body>
<main class="flyer">
  <div class="headline-word headline-top">GET FIT</div>
  <div class="headline-word headline-bottom">NOW</div>

  <p class="callout callout-trial">CONTACT US FOR A FREE TRIAL!</p>

  <figure class="snapshot snapshot-left"><div class="photo photo-ropes" role="img" aria-label="Athlete in a blue hoodie training with battle ropes outside the gym"></div></figure>
  <figure class="snapshot snapshot-center"><div class="photo photo-straps" role="img" aria-label="Group class doing suspension strap rows indoors"></div></figure>
  <figure class="snapshot snapshot-right"><div class="photo photo-sled" role="img" aria-label="Clients pulling and pushing weighted sleds on turf"></div></figure>

  <p class="callout callout-phone">CALL TODAY 718-403-5816</p>

  <section class="info-band">
    <ul class="contact-list">
      <li class="contact-item">
        <svg class="contact-icon" viewBox="0 0 30 40" aria-hidden="true"><path d="M15 38 C6 25 3 19 3 14 A12 12 0 0 1 27 14 C27 19 24 25 15 38 Z" fill="none" stroke="#2a2a2a" stroke-width="1.6"/><circle cx="15" cy="14" r="5" fill="none" stroke="#2a2a2a" stroke-width="1.6"/></svg>
        4-18 263rd Street<br>Whitestone NY, 11357
      </li>
      <li class="contact-item">
        <svg class="contact-icon" viewBox="0 0 30 30" aria-hidden="true"><circle cx="15" cy="15" r="12" fill="none" stroke="#2a2a2a" stroke-width="1.6"/><circle cx="15" cy="15" r="5" fill="none" stroke="#2a2a2a" stroke-width="1.6"/><path d="M20 11 V17 Q20 21 24 19" fill="none" stroke="#2a2a2a" stroke-width="1.6"/></svg>
        contact@quillathletic.com
      </li>
      <li class="contact-item">
        <svg class="contact-icon" viewBox="0 0 30 30" aria-hidden="true"><path d="M6 3 L24 18 L16 18 L20 27 L16 28 L12 19 L6 24 Z" fill="none" stroke="#2a2a2a" stroke-width="1.6" stroke-linejoin="round"/></svg>
        quillathletic.com
      </li>
    </ul>
    <div class="brand">
      <div class="brand-name"><span class="brand-dot"></span>Quill Athletics</div>
      <div class="brand-tagline">Personal Training Center</div>
    </div>
  </section>
</main>
</body>
</html>
```